Application Dashboard Skin - Non coded theme only

We are looking for a website color theme/look feel for a new .net dashboard application we are building. Target audience who will be using this are E and C level professionals. We are looking for the following:

Images of optional color themes for our existing dashboard. You can access a temporary version with no styling here: http://vantorquel.net:99/ . Application built in telerik and highcharts.

We are not looking for finished code or application skins. Our development team will take your final design (with specific colors/images/etc. provided) and apply it to the final beta version of the application.

Design considerations:
We are open to creative ideas, but please know that preference will be given to professional designs with emphasis on a consistent brand look/feel. Designs and colors should be focused on quickly identifying and processing the data.

Multiple submissions welcome.

-Pellowrin team

Target Market(s)

IT / Insurance

Industry/Entity Type

Building

Number of Pages Required

3 page

Requirements
Must have
• Application Dashboard link for design: http://vantorquel.net:99/

```html
<!DOCTYPE html>
<html lang="en">
<head>
<meta charset="utf-8">
<title>Ledgerview – Dashboard</title>
<link href="https://fonts.googleapis.com/css2?family=Roboto:wght@300;400;500;700&display=swap" rel="stylesheet">
<style>
:root{
  --orange:#f7941d;
  --orange-light:#fbb63a;
  --orange-dark:#d96a06;
  --brown:#a34d00;
  --header-bg:#e8e8e8;
  --text:#333;
  --muted:#666;
  --row-alt:#e6e6e6;
  --border:#d6d6d6;
  --grid:#e6e6e6;
  --bar-grey:#8c8c8c;
  --bar-blue:#7cb5ec;
  --pie-blue:#336ea6;
  --pie-navy:#0f457e;
  --footer-dark:#3a3a3a;
}
*{box-sizing:border-box;margin:0;padding:0}
html,body{width:1124px;height:1200px;overflow:hidden;background:#fff;font-family:'Roboto',sans-serif;color:var(--text)}
.canvas{position:relative;width:1124px;height:1200px}
.abs{position:absolute}
.topbar{left:0;top:0;width:1124px;height:95px;background:var(--header-bg)}
.brand{left:92px;top:38px;font-size:18px;font-weight:500;color:#333;letter-spacing:.2px}
.nav{top:43px;font-size:12px;color:#333;letter-spacing:.1px}
.panel-head{background:var(--orange);color:#fff;font-size:12px;font-weight:500;display:flex;align-items:center;justify-content:space-between;padding:0 15px}
.select{background:#fde9cc;color:#333;font-size:11.5px;font-weight:400;height:20px;display:flex;align-items:center;justify-content:space-between;padding:0 8px;width:99px}
.select::after{content:"";border:4px solid transparent;border-top:5px solid #444;border-bottom:0}
.kpi{left:92px;top:112px;width:258px;height:412px;border:1px solid var(--border)}
.kpi .panel-head{height:46px;padding:0 9px}
.kpi-title{text-align:center;font-size:16px;font-weight:500;margin-top:15px;line-height:21px;color:#333}
.kpi-title span{display:block;font-weight:500}
.kpi-rows{margin-top:13px}
.kpi-row{display:flex;height:27.3px;align-items:center;font-size:9.5px;padding-left:9px}
.kpi-row:nth-child(odd){background:var(--row-alt)}
.kpi-row i{width:8px;height:8px;border-radius:50%;background:var(--orange);margin-right:6px;flex:none}
.kpi-row .lbl{width:161px}
.box{border:1px solid var(--border);background:#fff}
.chart-title{position:absolute;width:100%;text-align:center;font-size:13.5px;letter-spacing:.5px}
.menu{position:absolute;width:12px;height:9px;border-top:2px solid #555;border-bottom:2px solid #555}
.menu::after{content:"";position:absolute;left:0;right:0;top:1.5px;border-top:2px solid #555}
.tabs{left:374px;top:596px;width:657px;height:37px;font-size:12px;color:#666}
.tab{position:absolute;top:0;height:38px;line-height:37px}
.tab.active{left:0;width:86px;border:1px solid var(--orange);border-bottom:1px solid #fff;background:#fff;color:var(--orange);text-align:center;z-index:2}
.error-panel{left:374px;top:632px;width:657px;height:289px;border:1px solid var(--orange)}
.social{top:1092px;width:36px;height:36px;border:1px solid #555;display:flex;align-items:center;justify-content:center}
.social i{width:10px;height:10px;background:var(--orange);border-radius:50%}
.copy{left:0;width:1124px;top:1150px;text-align:center;font-size:11.5px;color:#333;font-weight:300}
.footbar{left:0;top:1192px;width:1124px;height:8px;background:var(--footer-dark)}
svg text{font-family:'Roboto',sans-serif}
</style>
</head>
<body>
<div class="canvas">
  <header class="abs topbar"></header>
  <div class="abs brand">Ledgerview</div>
  <nav>
    <div class="abs nav" style="left:503px">ACCURACY RESULTS</div>
    <div class="abs nav" style="left:662px">PROCESSOR ACCURACY</div>
    <div class="abs nav" style="left:841px">MANAGE USERS</div>
    <div class="abs nav" style="left:976px">SETTINGS</div>
  </nav>

  <section class="abs kpi">
    <div class="panel-head">KPI'S <div class="select">All Regions</div></div>
    <div class="kpi-title">Overall YTD Accuracy<span>97.41%</span></div>
    <div class="kpi-rows">
      <div class="kpi-row"><i></i><span class="lbl">Claims Audited:</span>4859</div>
      <div class="kpi-row"><i></i><span class="lbl">Avg. Claims Audited per day:</span>6.7</div>
      <div class="kpi-row"><i></i><span class="lbl">Errors Found:</span>2147</div>
      <div class="kpi-row"><i></i><span class="lbl">Financial Impact:</span>$1,462,139</div>
      <div class="kpi-row"><i></i><span class="lbl">Total Claims Posted:</span>17,773,591</div>
      <div class="kpi-row"><i></i><span class="lbl">Total Encounter Claims:</span>93,984,586</div>
      <div class="kpi-row"><i></i><span class="lbl">Total Auto Adjudication:</span>920,918</div>
      <div class="kpi-row"><i></i><span class="lbl">Total Adjustment Claim Count:</span>920,918</div>
      <div class="kpi-row"><i></i><span class="lbl">Total Denied Claim Count:</span>133,523</div>
      <div class="kpi-row"><i></i><span class="lbl">Total Dollars Paid:</span>$5,669,835,044</div>
      <div class="kpi-row"><i></i><span class="lbl">Auto Adjudication Rate:</span>$0.052</div>
    </div>
  </section>

  <section class="abs box" style="left:93px;top:543px;width:256px;height:290px">
    <div class="chart-title" style="top:14px">Paid vs. Denied:</div>
    <div class="menu" style="left:224px;top:20px"></div>
    <svg width="256" height="290" style="position:absolute;left:0;top:0">
      <ellipse cx="127" cy="155" rx="103" ry="81" fill="var(--pie-blue)"/>
      <line x1="127" y1="155" x2="129" y2="74" stroke="#fff" stroke-width="1.5"/>
      <path d="M130 60 q-4 0 -4 10 v6" fill="none" stroke="var(--pie-blue)"/>
      <text x="143" y="57" font-size="9" font-weight="700">Denied: 0.7 %</text>
      <path d="M125 236 q0 10 -6 12" fill="none" stroke="var(--pie-blue)"/>
      <text x="46" y="260" font-size="9" font-weight="700">Paid: 99.3 %</text>
    </svg>
  </section>

  <section class="abs box" style="left:94px;top:844px;width:256px;height:235px">
    <div class="chart-title" style="top:12px;font-size:15px">Paid vs. Encounter:</div>
    <div class="menu" style="left:229px;top:20px"></div>
    <svg width="256" height="235" style="position:absolute;left:0;top:0">
      <circle cx="111" cy="100" r="35" fill="var(--pie-navy)"/>
      <path d="M111 100 L111 65 A35 35 0 0 0 81.6 81 Z" fill="var(--pie-blue)" stroke="#fff" stroke-width="1"/>
      <path d="M78 49 q8 6 14 20" fill="none" stroke="var(--pie-blue)"/>
      <text x="0" y="48" font-size="9.5" font-weight="700">Paid: 15.9 %</text>
      <path d="M128 130 q10 20 22 22" fill="none" stroke="var(--pie-navy)"/>
      <text x="154" y="156" font-size="9.5" font-weight="700">Encounter: 84.1 %</text>
    </svg>
  </section>

  <section class="abs panel-head" style="left:374px;top:113px;width:657px;height:45px">ACCURACY RESULTS <div class="select">End to end</div></section>

  <section class="abs box" style="left:374px;top:180px;width:657px;height:306px">
    <div class="chart-title" style="top:4px">YTD Overall Accuracy</div>
    <div class="chart-title" style="top:23px;font-size:8.5px;color:#555;letter-spacing:.2px">Click the bars to view YTD details for the specific region</div>
    <div class="menu" style="left:634px;top:14px"></div>
    <svg width="657" height="306" style="position:absolute;left:0;top:0">
      <g stroke="var(--grid)">
        <line x1="59" x2="650" y1="43" y2="43"/><line x1="59" x2="650" y1="87" y2="87"/>
        <line x1="59" x2="650" y1="131" y2="131"/><line x1="59" x2="650" y1="175" y2="175"/>
        <line x1="59" x2="650" y1="219" y2="219"/><line x1="59" x2="650" y1="263" y2="263" stroke="#ccc"/>
      </g>
      <g font-size="8.5" fill="#555" text-anchor="end">
        <text x="50" y="46">100</text><text x="50" y="90">97.5</text><text x="50" y="134">95</text>
        <text x="50" y="178">92.5</text><text x="50" y="222">90</text><text x="50" y="266">87.5</text>
      </g>
      <text transform="translate(16 153) rotate(-90)" font-size="8.5" fill="#555" text-anchor="middle">Overall Accuracy</text>
      <rect x="90" y="83.5" width="58" height="179.5" fill="var(--orange-light)"/>
      <rect x="208" y="69.4" width="58" height="193.6" fill="var(--orange)"/>
      <rect x="326" y="99.3" width="58" height="163.7" fill="var(--orange-dark)"/>
      <rect x="443" y="83.5" width="58" height="179.5" fill="var(--orange-light)"/>
      <rect x="561" y="132.8" width="58" height="130.2" fill="var(--brown)"/>
      <g font-size="8.5" font-weight="700" text-anchor="middle" text-decoration="underline" fill="#111">
        <text x="119" y="80">97.7%</text><text x="237" y="66">98.5%</text><text x="355" y="96">96.8%</text>
        <text x="472" y="80">97.7%</text><text x="590" y="129">94.9%</text>
        <text x="119" y="278">Colorado</text><text x="237" y="278">Georgia</text><text x="355" y="278">Hawaii</text>
        <text x="472" y="278">MidAtlantic</text><text x="590" y="278">NorthWest</text>
      </g>
    </svg>
  </section>

  <section class="abs panel-head" style="left:374px;top:522px;width:657px;height:45px">ERROR IMPACT FOR JUNE 2016 <div class="select">All Regions</div></section>

  <div class="abs tabs">
    <div class="tab active">All Errors</div>
    <div class="tab" style="left:132px">Providers</div>
    <div class="tab" style="left:246px">Employers</div>
    <div class="tab" style="left:365px">LineOfBusiness</div>
  </div>

  <section class="abs error-panel">
    <svg width="657" height="289" style="position:absolute;left:0;top:0">
      <g font-size="12.5" fill="#333" text-anchor="middle" letter-spacing=".4">
        <text x="161" y="21">Top 10 Error Reasons</text>
        <text x="475" y="21">Top 10 Error Reasons - Financial Impact</text>
      </g>
      <g font-size="7.5" fill="#555" text-anchor="middle"><text x="161" y="35">AllRegions</text><text x="478" y="35">AllRegions</text></g>
      <g stroke="#555" stroke-width="2"><path d="M290 22h11M290 26h11M290 30h11M608 22h11M608 26h11M608 30h11"/></g>
      <g font-size="7" fill="#555" text-anchor="end">
        <text x="125" y="61">INCORRECT CONTRACT…</text><text x="125" y="79">CLAIM PAID INCORRECT…</text>
        <text x="125" y="97">Not a Halvane benefit. Bill …</text><text x="125" y="115">INCORRECT CO-PAY / …</text>
        <text x="125" y="133">Copay Amount not corr…</text><text x="125" y="151">DID NOT FOLLOW DESK …</text>
        <text x="125" y="169">DID NOT FOLLOW PNP</text><text x="125" y="187">CLAIM DENIED IN ERRO…</text>
        <text x="125" y="205">Unknown</text><text x="125" y="223">DENIED INCORRECTLY -…</text>
        <text x="428" y="61">INCORRECT CONTRACT…</text><text x="428" y="79">CLAIM PAID INCORRECT…</text>
        <text x="428" y="97">Not a Halvane benefit. Bill …</text><text x="428" y="115">INCORRECT CO-PAY / …</text>
        <text x="428" y="133">Copay Amount not corr…</text><text x="428" y="151">DID NOT FOLLOW DESK …</text>
        <text x="428" y="169">DID NOT FOLLOW PNP</text><text x="428" y="187">CLAIM DENIED IN ERRO…</text>
        <text x="428" y="205">Unknown</text><text x="428" y="223">DENIED INCORRECTLY -…</text>
      </g>
      <text transform="translate(34 140) rotate(-90)" font-size="7" fill="#555" text-anchor="middle">AllErrors</text>
      <g stroke="var(--grid)"><line x1="137" x2="137" y1="48" y2="232"/><line x1="178" x2="178" y1="48" y2="232"/><line x1="218" x2="218" y1="48" y2="232"/><line x1="259" x2="259" y1="48" y2="232"/><line x1="299" x2="299" y1="48" y2="232"/></g>
      <g fill="var(--bar-grey)">
        <rect x="137" y="54" width="141" height="8"/><rect x="137" y="72" width="105" height="8"/>
        <rect x="137" y="90" width="97" height="8"/><rect x="137" y="108" width="93" height="8"/>
        <rect x="137" y="126" width="81" height="8"/><rect x="137" y="144" width="81" height="8"/>
        <rect x="137" y="162" width="77" height="8"/><rect x="137" y="180" width="57" height="8"/>
        <rect x="137" y="198" width="57" height="8"/><rect x="137" y="216" width="48" height="8"/>
      </g>
      <g font-size="7.5" font-weight="700" fill="#111">
        <text x="282" y="61">35</text><text x="246" y="79">26</text><text x="238" y="97">24</text><text x="234" y="115">23</text>
        <text x="222" y="133">20</text><text x="222" y="151">20</text><text x="218" y="169">19</text><text x="198" y="187">14</text>
        <text x="198" y="205">14</text><text x="189" y="223">12</text>
      </g>
      <g font-size="7" fill="#555" text-anchor="middle">
        <text x="137" y="243">0</text><text x="178" y="243">10</text><text x="218" y="243">20</text><text x="259" y="243">30</text><text x="299" y="243">40</text>
        <text x="218" y="256">Count</text>
      </g>
      <g stroke="var(--grid)"><line x1="444" x2="444" y1="48" y2="232"/><line x1="479" x2="479" y1="48" y2="232"/><line x1="514" x2="514" y1="48" y2="232"/><line x1="550" x2="550" y1="48" y2="232"/><line x1="585" x2="585" y1="48" y2="232"/><line x1="620" x2="620" y1="48" y2="232"/></g>
      <g fill="var(--bar-blue)">
        <rect x="470" y="54" width="137" height="8"/><rect x="538" y="72" width="52" height="8"/>
        <rect x="578" y="108" width="7" height="8"/><rect x="533" y="162" width="70" height="8"/>
        <rect x="585" y="180" width="9" height="8"/><rect x="585" y="216" width="2" height="8"/>
      </g>
      <g font-size="7.5" font-weight="700" fill="#111">
        <text x="473" y="61">$ -65155.67</text><text x="560" y="61">$ 12510.63</text>
        <text x="463" y="79">$ -26915.92</text><text x="544" y="79">$ 2919.39</text>
        <text x="553" y="97">$ -245</text><text x="599" y="97">$ 0</text>
        <text x="523" y="115">$ -3898.21</text>
        <text x="554" y="133">$ -295</text><text x="599" y="133">$ 10</text>
        <text x="572" y="151">$ 0</text><text x="599" y="151">$ 0</text>
        <text x="457" y="169">$ -29341.33</text><text x="555" y="169">$ 10390.26</text>
        <text x="572" y="187">$ 0</text>
        <text x="572" y="205">$ 0</text><text x="600" y="205">$ 331.1</text>
        <text x="551" y="223">$ -1.81</text>
      </g>
      <g font-size="7" fill="#555" text-anchor="middle">
        <text x="409" y="243">-80k</text><text x="444" y="243">-60k</text><text x="479" y="243">-40k</text><text x="514" y="243">-20k</text>
        <text x="550" y="243">0k</text><text x="585" y="243">20k</text><text x="531" y="256">$ Amount</text>
      </g>
    </svg>
  </section>

  <div class="abs social" style="left:452px"><i></i></div>
  <div class="abs social" style="left:499px"><i></i></div>
  <div class="abs social" style="left:545px"><i></i></div>
  <div class="abs social" style="left:592px"><i></i></div>
  <div class="abs social" style="left:638px"><i></i></div>

  <div class="abs copy">Copyrights © 2015-2016&nbsp; All Rights Reserved</div>
  <div class="abs footbar"></div>
</div>
</body>
</html>
```